Kestrel Plumbing business card full re design & logo design

Kestrel Plumbing is a Sydney based mechanical plumbing contractor company.
We would like a full redesign with new logo etc which we can take to a future website, uniforms, vehicle sign writing etc.
Blue is my preferred choice of colour but i would be open to see a couple of alternatives thrown in the mix to see how they compare. I am open to see on white cards, black cards etc. Open to many new ideas.
Please see attached original business cards which have been used for the last 5 years.

Target Market(s)

Mechanical services industry.

Industry/Entity Type

Plumbing

Contact Information for Business Card

Dale Fenmore
Director

Mob: 0427 596 418
Email: dale@kestrelplumbing-demo.net.au
PO BOX 782
Merrowvale NSW 2199
Lic: 518604k

Logo Text

Kestrel Plumbing

Font styles to use
Sans Serif

Colors
0655a3
3276b5
0792cd
33a6d7
85cae6
000000
333333
474747

Requirements
Must have
• Things that make it very professional and very well presented.
Nice to have
• Same description or very similar to attached uploaded file
Should not have
• Anything that makes it look unprofessional or cartoony.

```html
<!DOCTYPE html>
<html lang="en">
<head>
<meta charset="utf-8">
<title>Kestrel Plumbing — Business Card</title>
<link rel="stylesheet" href="https://fonts.googleapis.com/css2?family=Roboto+Condensed:wght@400;700&display=swap">
<style>
  :root {
    --navy: #06477b;
    --band: #76a0c6;
    --accent: #2f76b0;
    --ink: #1a1a1a;
    --paper: #ffffff;
    --stage: #e6e8eb;
    --mark: #cfe0ef;
  }
  * { box-sizing: border-box; margin: 0; padding: 0; }
  html, body { width: 1200px; height: 955px; overflow: hidden; }
  body {
    background: var(--stage);
    font-family: "Roboto Condensed", Arial, sans-serif;
    position: relative;
  }
  .card {
    position: absolute;
    left: 250px;
    width: 700px;
    height: 428px;
    overflow: hidden;
    box-shadow: 0 4px 14px rgba(0,0,0,.18);
  }

  /* Front */
  .card-front { top: 30px; background: var(--navy); }
  .front-mark {
    position: absolute;
    left: 0; right: 0; top: 120px;
    display: flex; align-items: center; justify-content: center; gap: 14px;
    color: var(--mark);
    font-weight: 700;
    font-size: 30px;
    letter-spacing: .5px;
    text-transform: uppercase;
  }
  .front-mark .dot { width: 22px; height: 22px; background: var(--mark); }
  .front-band {
    position: absolute;
    left: 0; right: 0; top: 302px; height: 74px;
    background: var(--band);
  }
  .front-band .notch { position: absolute; left: 346px; top: -22px; }
  .front-name {
    position: absolute;
    right: 40px; top: 302px; height: 74px;
    display: flex; align-items: center;
    color: var(--paper);
    font-weight: 700;
    font-size: 48px;
    letter-spacing: .5px;
    text-transform: uppercase;
  }

  /* Back */
  .card-back { top: 497px; background: var(--paper); }
  .back-panel {
    position: absolute; left: 0; top: 0; bottom: 0; width: 217px;
    background: var(--navy);
  }
  .back-strip {
    position: absolute; left: 217px; top: 0; bottom: 0; width: 44px;
    background: var(--band);
  }
  .back-strip .notch { position: absolute; left: 44px; top: 86px; }
  .back-brand {
    position: absolute;
    left: 108px; top: 214px;
    transform: translate(-50%, -50%) rotate(-90deg);
    display: flex; align-items: center; gap: 12px;
    white-space: nowrap;
    color: var(--paper);
    font-weight: 700;
    font-size: 22px;
    letter-spacing: .5px;
    text-transform: uppercase;
  }
  .back-brand .dot { width: 16px; height: 16px; border-radius: 50%; background: var(--paper); }

  .contact { position: absolute; left: 298px; top: 64px; right: 40px; color: var(--ink); }
  .contact-name { color: var(--accent); font-weight: 700; font-size: 32px; line-height: 1; }
  .contact-role { font-size: 24px; margin-top: 8px; }
  .licence { margin-top: 54px; color: var(--accent); font-weight: 700; font-size: 20px; }
  .trade { font-size: 21px; margin-top: 4px; text-transform: uppercase; }
  .address { margin-top: 36px; font-size: 20px; text-transform: uppercase; padding-bottom: 6px; border-bottom: 3px solid var(--accent); width: 330px; white-space: nowrap; }
  .phone { margin-top: 8px; font-size: 21px; letter-spacing: .5px; }
  .phone .sep { color: var(--accent); padding: 0 3px; }
  .email { font-size: 20px; margin-top: 2px; white-space: nowrap; }
</style>
</head>
<body>

<section class="card card-front" aria-label="Business card front">
  <div class="front-mark"><span class="dot"></span><span>Kestrel Plumbing</span></div>
  <div class="front-band">
    <svg class="notch" width="40" height="22" viewBox="0 0 40 22" aria-hidden="true"><polygon points="0,22 20,0 40,22" fill="#76a0c6"/></svg>
  </div>
  <div class="front-name">Kestrel Plumbing</div>
</section>

<section class="card card-back" aria-label="Business card back">
  <div class="back-panel"></div>
  <div class="back-strip">
    <svg class="notch" width="16" height="30" viewBox="0 0 16 30" aria-hidden="true"><polygon points="0,0 16,15 0,30" fill="#76a0c6"/></svg>
  </div>
  <div class="back-brand"><span class="dot"></span><span>Kestrel Plumbing</span></div>

  <div class="contact">
    <div class="contact-name">Dale Fenmore</div>
    <div class="contact-role">Director</div>
    <div class="licence">LIC: 518604k</div>
    <div class="trade">Mechanical Plumbing Contractor</div>
    <div class="address">PO Box 782 Merrowvale NSW 2199</div>
    <div class="phone">042<span class="sep">•</span>759<span class="sep">•</span>6418</div>
    <div class="email">Email: dale@kestrelplumbing-demo.net.au</div>
  </div>
</section>

</body>
</html>
```